Real estate broker business card

Want a modern celan but effective business card for my residential and commercial real estate business. I want the back of the card to advertise my services and to capture business. I have attached the back of my current business card fore ideas
Updates

Target Market(s)

home buyers and seller. commercial buyers and sellers

Industry/Entity Type

Real Estate

Contact Information for Business Card

must have my contact information and my photo

Requirements
Must have
• Lorna Vettridge
• Owner & Qualifying Broker
• Brockhill Real Estate Services
• 555.218.7094
• lorna@brockhillhomes.example
• www.brockhillhomes.example
Nice to have
• metallic
• Business capture text: " Don't buy or lease property without someone looking out for your best interests. I will represent you on your home or investment purchase for FREE!"
• "Home owners, call today to receive a FREE market analysis for your homes value!

```html
<!DOCTYPE html>
<html lang="en">
<head>
<meta charset="utf-8">
<title>Brockhill Real Estate Services – Business Card</title>
<link rel="stylesheet" href="https://fonts.googleapis.com/css2?family=Arimo:wght@400;700&display=swap">
<style>
  :root {
    --page: #ffffff;
    --ink: #1b1b1d;
    --card-dark: #161719;
    --card-light: #ffffff;
    --accent-green: #2aaa8f;
    --brand-teal: #1d8497;
    --card-outline: #3a3a3a;
    --silver-dark: #3b3b3d;
    --silver-light: #f2f2f2;
  }
  html, body {
    margin: 0;
    width: 1200px;
    height: 1200px;
    overflow: hidden;
    background: var(--page);
  }
  .canvas {
    position: relative;
    width: 1200px;
    height: 1200px;
  }
  .card {
    position: absolute;
    left: 180px;
    width: 838px;
    height: 480px;
  }
  .card--front { top: 98px; }
  .card--back { top: 621px; }
  .card svg { display: block; }
  .brand-name {
    font-family: "Arimo", Arial, sans-serif;
    font-weight: 700;
    fill: var(--brand-teal);
  }
  .person-name {
    font-family: "Arimo", Arial, sans-serif;
    font-weight: 700;
    font-size: 34px;
    fill: var(--ink);
  }
  .person-title,
  .contact-text {
    font-family: "Arimo", Arial, sans-serif;
    font-weight: 400;
    fill: var(--ink);
  }
  .person-title { font-size: 22px; }
  .contact-text { font-size: 23px; }
  .contact-icon { fill: none; stroke: var(--accent-green); stroke-width: 2; }
  .contact-icon--solid { fill: var(--accent-green); stroke: none; }
</style>
</head>
<body>
<main class="canvas">

  <!-- Front face -->
  <section class="card card--front" aria-label="Card front">
    <svg width="838" height="480" viewBox="0 0 838 480">
      <defs>
        <clipPath id="front-shape"><rect width="838" height="480" rx="40"/></clipPath>
        <linearGradient id="silver-swoosh" x1="0" y1="0" x2="1" y2="0">
          <stop offset="0" stop-color="var(--silver-dark)"/>
          <stop offset="0.45" stop-color="var(--silver-light)"/>
          <stop offset="0.7" stop-color="#9a9a9c"/>
          <stop offset="1" stop-color="var(--silver-dark)"/>
        </linearGradient>
      </defs>
      <g clip-path="url(#front-shape)">
        <rect class="card-base" width="838" height="480" fill="var(--card-dark)"/>
        <path class="accent-band" d="M0,412 C220,450 560,370 838,194 L838,480 L0,480 Z" fill="var(--accent-green)"/>
        <path class="metal-swoosh" d="M20,404 C250,418 570,358 798,206 C600,356 270,440 20,404 Z" fill="url(#silver-swoosh)"/>
      </g>
      <rect class="brand-mark" x="150" y="108" width="112" height="112" fill="var(--brand-teal)"/>
      <text class="brand-name" x="296" y="202" font-size="66" letter-spacing="3">BROCKHILL</text>
      <text class="brand-name" x="297" y="234" font-size="22" letter-spacing="6.4">REAL ESTATE SERVICES</text>
    </svg>
  </section>

  <!-- Back face -->
  <section class="card card--back" aria-label="Card back">
    <svg width="838" height="480" viewBox="0 0 838 480">
      <defs>
        <clipPath id="back-shape"><rect width="838" height="480" rx="40"/></clipPath>
      </defs>
      <g clip-path="url(#back-shape)">
        <rect class="card-base" width="838" height="480" fill="var(--card-light)"/>
        <path class="accent-band" d="M0,412 C220,450 560,370 838,194 L838,480 L0,480 Z" fill="var(--accent-green)"/>
        <path class="white-gap" d="M0,408 C230,440 560,366 838,190 L838,198 C560,376 220,456 0,418 Z" fill="var(--card-light)"/>
        <path class="metal-swoosh" d="M20,404 C250,418 570,358 798,206 C600,356 270,440 20,404 Z" fill="url(#silver-swoosh)"/>
      </g>
      <rect x="0.5" y="0.5" width="837" height="479" rx="40" fill="none" stroke="var(--card-outline)" stroke-width="1"/>

      <text class="person-name" x="54" y="142">Lorna Vettridge</text>
      <text class="person-title" x="54" y="171">Owner &amp; Qualifying Broker</text>

      <rect class="brand-mark" x="416" y="68" width="84" height="84" fill="var(--brand-teal)"/>
      <text class="brand-name" x="520" y="140" font-size="46" letter-spacing="2">BROCKHILL</text>
      <text class="brand-name" x="521" y="166" font-size="16" letter-spacing="4.3">REAL ESTATE SERVICES</text>

      <g class="contact-list">
        <rect class="contact-icon" x="53" y="259" width="14" height="22" rx="3"/>
        <circle class="contact-icon--solid" cx="60" cy="276" r="1.6"/>
        <text class="contact-text" x="90" y="279">555.218.7094</text>

        <rect class="contact-icon--solid" x="49" y="306" width="22" height="14"/>
        <path d="M49,306 L60,315 L71,306 M49,320 L57,313 M71,320 L63,313" stroke="#fff" stroke-width="1.5" fill="none"/>
        <text class="contact-text" x="90" y="319">lorna@brockhillhomes.example</text>

        <circle class="contact-icon" cx="61" cy="350" r="9.5"/>
        <ellipse class="contact-icon" cx="61" cy="350" rx="4" ry="9.5"/>
        <path class="contact-icon" d="M51.5,350 H70.5 M53,345 H69 M53,355 H69"/>
        <text class="contact-text" x="90" y="358">www.brockhillhomes.example</text>
      </g>
    </svg>
  </section>

</main>
</body>
</html>
```